Wirenexa

I'm looking to much improve our current website wirenexa.com
Updates

Low design quality

Target Market(s)

Commercial clients (Not-Residentials)

Industry/Entity Type

Office buildings and Industrial clients

Coding

Coded - Design and coding required

Number of Pages Required

5+ page

Requirements
Must have
• Very professional structured low voltage cabling projects for Wi-Fi, Audio/Video conference rooms, Access Control systems, CCTV.

```html
<!DOCTYPE html>
<html lang="en">
<head>
<meta charset="utf-8">
<title>Wirenexa – About Us</title>
<link rel="stylesheet" href="https://fonts.googleapis.com/css2?family=Montserrat:wght@600;700&family=Roboto:wght@400;500;700&display=swap">
<style>
:root{
  --red:#d3202a;
  --red-soft:#fde8e9;
  --ink:#1b1d24;
  --body:#4b5160;
  --muted:#6b7280;
  --line:#e6e8ec;
  --band:#f1f2f4;
  --footer:#1c2130;
  --footer-card:#242a3a;
  --footer-text:#c4c8d2;
  --white:#ffffff;
}
*{box-sizing:border-box;margin:0;padding:0}
html,body{width:1200px;height:2383px;overflow:hidden;background:var(--white)}
body{font-family:"Roboto",Arial,sans-serif;color:var(--body)}
.stage{position:absolute;left:0;top:0;width:1300px;height:2582px;transform:scale(0.923077);transform-origin:0 0;background:#f7f7f8}
.page{position:absolute;left:20px;top:22px;width:1256px;height:2533px;background:var(--white);overflow:hidden}
.abs{position:absolute}
h1,h2,h3,h4{font-family:"Montserrat",Arial,sans-serif;color:var(--ink)}

/* header */
.site-header{left:0;top:0;width:1256px;height:70px;background:var(--white)}
.brand{display:flex;align-items:center;gap:8px;font-family:"Roboto",Arial,sans-serif;font-weight:700;font-size:28px;color:var(--ink)}
.brand-mark{width:24px;height:24px;background:var(--red);border-radius:3px}
.site-header .brand{position:absolute;left:92px;top:19px}
.nav{position:absolute;left:739px;top:27px;display:flex;gap:28px;font-size:13px;color:#374151}
.nav .active{color:var(--red)}
.btn{background:var(--red);color:var(--white);font-weight:500;border-radius:6px;display:flex;align-items:center;justify-content:center}
.btn-quote{position:absolute;left:1026px;top:16px;width:118px;height:35px;font-size:13px}

/* hero */
.hero{left:0;top:70px;width:1256px;height:240px;background:linear-gradient(100deg,#2d3744 0%,#4a5563 45%,#7b8390 75%,#a8adb6 100%)}
.hero-text{position:absolute;left:112px;top:55px;color:var(--white)}
.crumbs{font-size:12px;color:#d1d5db}
.crumbs b{color:var(--white);font-weight:700;margin-left:10px}
.crumbs span{margin-left:10px}
.hero h1{color:var(--white);font-size:32px;font-weight:700;margin-top:10px}
.hero p{font-size:15px;line-height:25px;margin-top:18px;width:560px}

/* why */
.pill{left:130px;top:441px;width:125px;height:21px;border:1px solid #f5b7ba;background:var(--red-soft);color:var(--red);border-radius:11px;font-size:8.5px;font-weight:500;display:flex;align-items:center;justify-content:center}
.why-title{left:130px;top:476px;font-size:32px;font-weight:700}
.why-copy{left:130px;top:543px;width:476px;font-size:14px;line-height:22.7px}
.why-copy p{margin-bottom:20px}
.why-copy p.lead{font-size:16.3px;line-height:25.3px;margin-bottom:16px}
.why-copy strong{color:#2b2f38;font-weight:700}
.photo{border-radius:10px;border:1px solid #d8dbe0}
.ph-sfp{left:688px;top:482px;width:229px;height:260px;background:linear-gradient(150deg,#c2541a 0%,#3a2a24 40%,#111 100%)}
.ph-meeting{left:932px;top:440px;width:229px;height:173px;background:linear-gradient(160deg,#dfe2e4,#9aa0a5 60%,#5c6166)}
.ph-patch{left:688px;top:758px;width:229px;height:172px;background:linear-gradient(135deg,#1a2a2e,#2b8c9a 55%,#0f1d21)}
.ph-fiber{left:932px;top:628px;width:229px;height:260px;background:radial-gradient(circle at 60% 40%,#4f7dff,#1433c9 55%,#050a4a)}
.badges{left:751px;top:983px;width:374px;height:77px;background:#f1f2f4;border-radius:8px;display:grid;grid-template-columns:183px 180px;padding:12px 0 0 21px;row-gap:12px;font-size:12px;color:#1f2430;font-weight:500}
.badges div{display:flex;align-items:center;gap:10px;height:19px}

/* partner */
.arch{left:130px;top:1358px;width:425px;height:385px;background:#f1f2f4;border-radius:213px 213px 0 0}
.rack{left:255px;top:1265px;width:185px;height:395px;background:linear-gradient(90deg,#6b6d70,#8c8e91 45%,#cfd0d2 70%,#9a9c9f);border-radius:4px}
.partner-title{left:677px;top:1408px;font-size:28px;line-height:42px;font-weight:700;width:470px}
.partner-copy{left:680px;top:1516px;width:450px;font-size:17px;line-height:26.3px;color:#3f4450}

/* emergency */
.band{left:0;top:1743px;width:1256px;height:308px;background:var(--band)}
.alert-card{left:113px;top:1813px;width:1030px;height:163px;background:var(--white);border-radius:10px;box-shadow:0 2px 8px rgba(20,25,40,.05)}
.alert-icon{position:absolute;left:112px;top:42px;width:62px;height:61px;background:var(--red-soft);border-radius:8px;display:flex;align-items:center;justify-content:center}
.alert-card h3{position:absolute;left:196px;top:40px;font-size:21px;font-weight:700}
.alert-card p{position:absolute;left:196px;top:76px;width:500px;font-size:13.5px;line-height:23px;color:var(--muted)}
.btn-connect{position:absolute;left:801px;top:83px;width:100px;height:30px;font-size:12.5px;border-radius:4px}

/* footer */
.site-footer{left:0;top:2050px;width:1256px;height:483px;background:var(--footer);color:var(--footer-text)}
.f-brand{position:absolute;left:92px;top:57px;width:155px;height:38px;background:#e7e7e9;border-radius:2px;display:flex;align-items:center;justify-content:center;gap:6px;font-weight:700;font-size:23px;color:var(--ink)}
.f-brand .brand-mark{width:18px;height:18px}
.f-about{position:absolute;left:92px;top:118px;width:240px;font-size:12px;line-height:20.3px}
.socials{position:absolute;left:92px;top:211px;display:flex;gap:14px}
.socials span{width:31px;height:31px;background:var(--white);border-radius:4px;display:flex;align-items:center;justify-content:center}
.socials i{width:11px;height:11px;background:#9ca3af;border-radius:2px}
.f-col h4{color:var(--white);font-size:16px;font-weight:700}
.f-services{position:absolute;left:370px;top:58px}
.f-services ul{list-style:none;margin-top:20px;font-size:12px}
.f-services li{height:28px;display:flex;align-items:center;gap:10px}
.f-offices{position:absolute;left:649px;top:58px}
.office{display:flex;gap:13px;font-size:12px;line-height:17px}
.office small{display:block;font-size:8px;font-weight:700;letter-spacing:.6px;color:var(--white)}
.anniv{position:absolute;left:925px;top:55px;width:112px;height:112px;background:var(--white);border-radius:6px;display:flex;align-items:center;justify-content:center}
.anniv div{width:76px;height:76px;border-radius:50%;background:linear-gradient(135deg,#1e9be0,#8bc53f 50%,#e6332a)}
.cert{position:absolute;left:925px;top:195px;width:237px;height:143px;background:var(--footer-card);border:1px solid #343b4d;border-radius:10px;padding:30px 20px 0 21px;font-size:12px;line-height:20.3px}
.cert b{color:var(--white)}
.f-rule{position:absolute;left:92px;top:385px;width:1073px;height:1px;background:#394052}
.f-bottom{position:absolute;left:92px;top:428px;width:1073px;display:flex;justify-content:space-between;font-size:10px;color:#9aa0ad;font-weight:500}
.f-bottom nav{display:flex;gap:21px;margin-left:60px}
</style>
</head>
<body>
<div class="stage">
<div class="page">

  <header class="site-header abs">
    <div class="brand"><span class="brand-mark"></span>Wirenexa</div>
    <nav class="nav"><span>Home</span><span class="active">About Us</span><span>Services</span><span>Contact</span></nav>
    <div class="btn btn-quote">Request a Quote</div>
  </header>

  <section class="hero abs" role="img" aria-label="Technician holding a tablet beside network server equipment">
    <div class="hero-text">
      <div class="crumbs">Home<span>›</span><b>About Us</b></div>
      <h1>Wirenexa: Your Trusted Cabling Partner</h1>
      <p>Wirenexa is a leading infrastructure cabling company dedicated to building, managing, securing, and supporting Information Technology infrastructure.</p>
    </div>
  </section>

  <div class="pill abs">Our Mission &amp; Vision</div>
  <h2 class="why-title abs">Why Choose Wirenexa?</h2>
  <div class="why-copy abs">
    <p class="lead"><strong>Decades of Experience:</strong> With decades of experience in Information Technology, Wirenexa brings unparalleled expertise to every project. Our seasoned professionals have the knowledge and skills to deliver efficient, results-oriented solutions tailored to your specific needs.</p>
    <p><strong>Top-Notch Customer Service:</strong> At Wirenexa, customer satisfaction is our top priority. We pride ourselves on delivering top-notch customer service and support to ensure that your technology needs are met with excellence and professionalism.</p>
    <p><strong>Nationwide Reach:</strong> Since our founding in 1994, we have successfully assisted hundreds of companies and organizations nationwide in building, managing, and supporting their IT systems. Our extensive experience spans various industries and sectors, making us a trusted partner for businesses of all sizes.</p>
    <p><strong>Diverse Clientele:</strong> Wirenexa serves a diverse clientele, including small, mid-size, and larger businesses across various industries. Many of our customer relationships have lasted for more than two decades, a testament to the quality and reliability of our services.</p>
    <p><strong>Commercial and Government Expertise:</strong> We have a proven track record of working with both commercial and government entities, including esteemed organizations such as Harborview Health, Lumen Theatres, Deskpoint, State Agriculture Office, and many more. Our extensive experience in these sectors allows us to understand and address unique challenges and requirements effectively.</p>
  </div>

  <div class="photo ph-sfp abs" role="img" aria-label="Close-up of a fiber transceiver module and network cable"></div>
  <div class="photo ph-meeting abs" role="img" aria-label="Business team meeting in a bright office"></div>
  <div class="photo ph-patch abs" role="img" aria-label="Patch panel filled with teal network cables"></div>
  <div class="photo ph-fiber abs" role="img" aria-label="Glowing blue fiber optic strands"></div>

  <div class="badges abs">
    <div><svg width="17" height="17" viewBox="0 0 17 17"><circle cx="8.5" cy="8.5" r="7.5" fill="none" stroke="#1f2430" stroke-width="1.3"/><path d="M5.3 8.7l2.2 2.1 4.2-4.3" fill="none" stroke="#1f2430" stroke-width="1.3"/></svg>Licensed &amp; Bonded</div>
    <div><svg width="17" height="17" viewBox="0 0 17 17"><circle cx="8.5" cy="8.5" r="7.5" fill="none" stroke="#1f2430" stroke-width="1.3"/><path d="M5.3 8.7l2.2 2.1 4.2-4.3" fill="none" stroke="#1f2430" stroke-width="1.3"/></svg>Full System Warranty</div>
    <div><svg width="17" height="17" viewBox="0 0 17 17"><circle cx="8.5" cy="8.5" r="7.5" fill="none" stroke="#1f2430" stroke-width="1.3"/><path d="M5.3 8.7l2.2 2.1 4.2-4.3" fill="none" stroke="#1f2430" stroke-width="1.3"/></svg>24/7 Support Desk</div>
    <div><svg width="17" height="17" viewBox="0 0 17 17"><circle cx="8.5" cy="8.5" r="7.5" fill="none" stroke="#1f2430" stroke-width="1.3"/><path d="M5.3 8.7l2.2 2.1 4.2-4.3" fill="none" stroke="#1f2430" stroke-width="1.3"/></svg>Design-Build Focus</div>
  </div>

  <div class="arch abs"></div>
  <svg class="abs" style="left:500px;top:1318px" width="180" height="110" viewBox="0 0 180 110"><path d="M10 105 H82 Q88 105 88 99 V46 Q88 40 94 40 H155" fill="none" stroke="#eceef1" stroke-width="5"/><path d="M150 29 L169 40 L150 51 Z" fill="#eceef1"/></svg>
  <div class="rack abs" role="img" aria-label="Illustration of a figure working at a server rack"></div>

  <h2 class="partner-title abs">Partner with Wirenexa for Strategic Technology Solutions</h2>
  <p class="partner-copy abs">Experience the difference that Wirenexa’s cabling services can make for your business. Contact us today to learn more about how we can build your IT infrastructure and drive your organization’s success.</p>

  <section class="band abs"></section>
  <div class="alert-card abs">
    <div class="alert-icon"><svg width="34" height="34" viewBox="0 0 34 34"><circle cx="17" cy="17" r="14.5" fill="none" stroke="#d3202a" stroke-width="2.4"/><path d="M17 9.5v9.5" stroke="#d3202a" stroke-width="2.6" stroke-linecap="round"/><circle cx="17" cy="24" r="1.7" fill="#d3202a"/></svg></div>
    <h3>Need Emergency Network Support?</h3>
    <p>We provide 24/7 critical infrastructure support for enterprise clients. If your business is facing a complete network outage, call our priority line immediately.</p>
    <div class="btn btn-connect">Quick Connect</div>
  </div>

  <footer class="site-footer abs">
    <div class="f-brand"><span class="brand-mark"></span>Wirenexa</div>
    <p class="f-about">The Mid-Atlantic’s premier provider of specialized low-voltage infrastructure since 1994. Quality, reliability, and precision in every connection.</p>
    <div class="socials"><span><i></i></span><span><i></i></span><span><i></i></span><span><i></i></span></div>

    <div class="f-col f-services">
      <h4>Services</h4>
      <ul>
        <li>›<span>Commercial Cabling</span></li>
        <li>›<span>Fiber Optic Installation</span></li>
        <li>›<span>Security &amp; CCTV</span></li>
        <li>›<span>VOIP &amp; Audio Visual</span></li>
        <li>›<span>Wi-Fi Site Surveys</span></li>
      </ul>
    </div>

    <div class="f-col f-offices">
      <h4>Our Offices</h4>
      <div class="office" style="margin-top:22px"><svg width="15" height="17" viewBox="0 0 15 17"><path d="M7.5 16s5.5-5.2 5.5-9A5.5 5.5 0 0 0 2 7c0 3.8 5.5 9 5.5 9z" fill="none" stroke="#e0353e" stroke-width="1.4"/><circle cx="7.5" cy="7" r="2" fill="none" stroke="#e0353e" stroke-width="1.4"/></svg><div><small>MAIN OFFICE (VA)</small>4120 Elm Ridge Dr, Suite 300,<br>Fairhaven, VA 22100</div></div>
      <div class="office" style="margin-top:24px"><svg width="15" height="17" viewBox="0 0 15 17"><path d="M7.5 16s5.5-5.2 5.5-9A5.5 5.5 0 0 0 2 7c0 3.8 5.5 9 5.5 9z" fill="none" stroke="#e0353e" stroke-width="1.4"/><circle cx="7.5" cy="7" r="2" fill="none" stroke="#e0353e" stroke-width="1.4"/></svg><div><small>REGIONAL OFFICE (MD)</small>2750 Millstone Pkwy,<br>Greenfield, MD 21000</div></div>
      <div class="office" style="margin-top:24px"><svg width="15" height="15" viewBox="0 0 15 15"><path d="M3 1.5l2.5.3 1 3-1.6 1.2a8 8 0 0 0 4 4l1.2-1.6 3 1 .3 2.5c-.3.9-1.1 1.6-2 1.6A11.5 11.5 0 0 1 1.4 3.5c0-.9.7-1.7 1.6-2z" fill="none" stroke="#e0353e" stroke-width="1.3"/></svg><div>Local: (555) 014-2200<br>National: (555) 019-7700</div></div>
      <div class="office" style="margin-top:20px"><svg width="15" height="13" viewBox="0 0 15 13"><rect x="1" y="1.5" width="13" height="10" rx="1.5" fill="none" stroke="#e0353e" stroke-width="1.3"/><path d="M1.5 2.5l6 4.5 6-4.5" fill="none" stroke="#e0353e" stroke-width="1.3"/></svg><div>sales@wirenexa.com</div></div>
    </div>

    <div class="anniv"><div></div></div>
    <div class="cert">Wirenexa is a proud employer of <b>Certified Network Infrastructure Designers (CNID),</b> ensuring industry-leading standards on every installation.</div>

    <div class="f-rule"></div>
    <div class="f-bottom">
      <span>© 2024 Wirenexa. All Rights Reserved. Licensed in VA, MD &amp; DC.</span>
      <nav><span>Privacy Policy</span><span>Terms of Service</span><span>Sitemap</span></nav>
      <span>Powered by Northline Web Studio</span>
    </div>
  </footer>

</div>
</div>
</body>
</html>
```